A Chatterloop Ad design to promote Laptops / Zephyrpad

I need a Chatterloop ad design (modifications to the attached file) . The laptop image needs to be a vector/illustration.Cannot use Zephyrpad actual image. Colour theme to remain as White, Black Grey (as per this image). Ad text [1st Line : For SME Business only! 2nd Line : Buy a new laptop with KTR Grant subsidy. 3rd line: Message us to find out more!] The overall feel should be similar to this image attached. As for the color/image in the laptop - pls try to suggest something similar to what Orvel uses for their ad.

Font styles to use
Sans Serif

Requirements
Must have
• The laptop image needs to be a vector/illustration.Cannot use Zephyrpad actual image. Colour theme to remain as White, Black Grey (as per this image). Ad text [1st Line : For SME Business only! 2nd Line : Buy a new laptop with KTR Grant subsidy. 3rd line: Message us to find out more!] The overall feel should be similar to this image attached.

```html
<!DOCTYPE html>
<html lang="en">
<head>
<meta charset="utf-8">
<title>KTR Grant Laptop Ad</title>
<link rel="stylesheet" href="https://fonts.googleapis.com/css2?family=Cabin:wght@400;500;700&display=swap">
<style>
  :root {
    --stage: #e6e6e6;
    --card: #ffffff;
    --ink: #111111;
    --ink-soft: #4a4a4a;
    --muted: #8a8a8a;
    --art-deep: #1b1630;
    --art-mid: #6a3d8f;
    --art-glow: #e08ad6;
    --silver: #cfcfd2;
  }
  * { margin: 0; padding: 0; box-sizing: border-box; }
  html, body {
    width: 1200px;
    height: 900px;
    overflow: hidden;
    background: var(--stage);
    font-family: "Cabin", sans-serif;
  }
  .ad {
    position: absolute;
    left: 160px;
    top: 10px;
    width: 880px;
    height: 880px;
    background: var(--card);
  }
  .ad__line {
    position: absolute;
    left: 0;
    width: 100%;
    text-align: center;
    line-height: 1;
  }
  .ad__eyebrow {
    top: 78px;
    font-size: 30px;
    color: var(--muted);
  }
  .ad__headline {
    top: 118px;
    font-size: 78px;
    font-weight: 700;
    letter-spacing: -0.5px;
    background: linear-gradient(180deg, var(--ink-soft) 0%, var(--ink) 55%, #000 100%);
    -webkit-background-clip: text;
    background-clip: text;
    color: transparent;
  }
  .ad__offer {
    top: 232px;
    font-size: 46px;
    line-height: 61px;
    color: var(--ink);
  }
  .ad__visual {
    position: absolute;
    left: 56px;
    top: 363px;
    width: 768px;
    height: 380px;
    border-radius: 10px 10px 6px 6px;
    background:
      radial-gradient(ellipse at 32% 70%, var(--art-glow) 0%, var(--art-mid) 28%, var(--art-deep) 60%, transparent 78%),
      linear-gradient(180deg, #2a2a2e 0%, #111 82%, var(--silver) 90%, #f2f2f2 100%);
  }
  .ad__cta {
    top: 790px;
    font-size: 34px;
    color: var(--muted);
  }
</style>
</head>
<body>
  <main class="ad">
    <p class="ad__line ad__eyebrow">For</p>
    <h1 class="ad__line ad__headline">SME Business Only!</h1>
    <p class="ad__line ad__offer">Buy a new laptop with<br>KTR Grant subsidy.</p>
    <div class="ad__visual" role="img" aria-label="Vector illustration of an open silver laptop with a purple and pink aurora wallpaper on screen"></div>
    <p class="ad__line ad__cta">Message us to find out more!</p>
  </main>
</body>
</html>
```